Packaging label for spirit line

We currently have a various line of spirits and are looking to rebrand the label. The bottle would stay the same since there is a lot of stock. An example of the current situation has been attached. The entire collection is to be found on our website: www.velvetroom.mardenhq.be/spirits

These spirits are a product created by our cocktail bar "Velvet Room". The name however, would likely change to "Tipplecat" or plural "Tipplecats" since we'd like to split those 2 businesses. The series "bartender series" would remain the same as it is a complete series mainly invented for mixology.

The current label is fine, but needs that extra spark that makes it stand out on a shelve compared to other spirit bottles. We envision a more funky yet sophisticated branding with perhaps goldtrims for that "exclusive, luxurious" feel and very much like a vintage animal humification vibe (for example: the quillmark or brenna's). Preferably a french bulldog as this has been our mascotte since the very beginning of starting this business.

Last but not least, the measurements: max. 90 mm height and max. 260 mm length. The current label is 90x180mm. 260mm means the label goes fully around the bottle.

Industry/Entity Type

Alcoholic Beverages

Font styles to use
Serif
Sans Serif

Requirements
Must have
• The label must have the standard information such as the product name, the alcohol %, the volume ml and room for ean code. The bottle needs to be sealed for shipment, so a little seal to cover the lid is required.
Nice to have
• It would be nice to maintain consistency with for example the same animal but change of background / colors / outfit / etc to clarify the different flavors. A cutout/contour is also preferable for added interest, so that the label is not square.
Should not have
• The label should definitely not be childish or too much. The overal look and feel needs to be professional yet not too serious.

```html
<!DOCTYPE html>
<html lang="en">
<head>
<meta charset="utf-8">
<title>Tipplecats London Dry Gin – Thymewise Label</title>
<link href="https://fonts.googleapis.com/css2?family=Open+Sans:wght@400;600;700&family=Cormorant+Garamond:wght@400;500&family=Parisienne&display=swap" rel="stylesheet">
<style>
  :root {
    --backdrop: #ecedef;
    --label-cream: #f4f2da;
    --label-edge: #e0dcbc;
    --brand-green: #2f7d36;
    --ink: #1b1b1b;
    --muted: #8c8a78;
    --rule: #c9c6aa;
    --herb-light: #e4e7c6;
    --herb-mid: #c3cf9c;
    --base-band: #3d3d3a;
  }
  * { box-sizing: border-box; margin: 0; padding: 0; }
  html, body { width: 1200px; height: 1200px; overflow: hidden; }
  body {
    background: var(--backdrop);
    position: relative;
    font-family: "Open Sans", sans-serif;
    color: var(--ink);
    font-variant-numeric: lining-nums;
  }
  .seal-strip {
    position: absolute;
    left: 560px; top: 10px;
    width: 80px; height: 200px;
    background: var(--label-cream);
    border-left: 3px dotted var(--label-edge);
    border-right: 3px dotted var(--label-edge);
    display: flex; align-items: center; justify-content: center;
  }
  .seal-strip span {
    writing-mode: vertical-rl;
    white-space: nowrap;
    font-family: "Cormorant Garamond", serif;
    font-size: 21px;
    color: var(--brand-green);
    letter-spacing: 1px;
  }
  .label {
    position: absolute;
    left: 220px; top: 210px;
    width: 760px; height: 890px;
    background: var(--label-cream);
    background-image: repeating-linear-gradient(90deg, rgba(0,0,0,0.025) 0 2px, transparent 2px 6px);
  }
  .label-edge { position: absolute; left: 0; width: 760px; height: 14px; }
  .label-edge.top { top: -13px; }
  .label-edge.bottom { bottom: -13px; }
  .herb-artwork {
    position: absolute; left: 0; top: 0;
    width: 90px; height: 860px;
    background: linear-gradient(180deg, var(--herb-light), var(--herb-mid) 55%, var(--herb-light));
    opacity: 0.8;
  }
  .brand {
    position: absolute; left: 0; right: 0; top: 100px;
    text-align: center;
  }
  .brand-name {
    display: inline-flex; align-items: center; gap: 16px;
    font-family: "Cormorant Garamond", serif;
    font-weight: 500;
    font-size: 54px;
    letter-spacing: 3px;
    color: var(--brand-green);
  }
  .brand-name .dot {
    width: 30px; height: 30px; border-radius: 50%;
    background: var(--brand-green);
  }
  .brand-tagline {
    margin-top: 6px;
    font-size: 13px; letter-spacing: 3px;
    color: var(--brand-green);
  }
  .product-type {
    position: absolute; left: 90px; right: 0; top: 290px;
    text-align: center;
    font-weight: 600; font-size: 68px; letter-spacing: -1px;
  }
  .description {
    position: absolute; left: 90px; right: 0; top: 410px;
    text-align: center;
    font-family: "Cormorant Garamond", serif;
    font-size: 26px; line-height: 38px;
    color: var(--muted);
  }
  .spec-table {
    position: absolute; left: 130px; right: 30px; top: 560px;
    height: 300px;
    border-top: 1px solid var(--rule);
  }
  .flavour {
    position: absolute; left: 0; right: 0; top: 0;
    text-align: center;
    font-family: "Parisienne", cursive;
    font-size: 80px; line-height: 120px;
    color: var(--ink);
  }
  .spec-row {
    position: absolute; left: 0; right: 0; top: 120px; bottom: 0;
    border-top: 1px solid var(--rule);
  }
  .batch {
    position: absolute; left: 0; top: 0; bottom: 0; width: 140px;
    border-right: 1px solid var(--rule);
    text-align: center;
    font-family: "Cormorant Garamond", serif;
    font-size: 46px; line-height: 60px;
    padding-top: 30px;
    color: var(--muted);
  }
  .category {
    position: absolute; left: 170px; top: 14px;
    font-size: 22px; letter-spacing: 6px; font-weight: 600;
  }
  .volume {
    position: absolute; left: 140px; right: 0; top: 62px;
    border-top: 1px solid var(--rule);
    padding: 22px 0 0 30px;
    font-family: "Cormorant Garamond", serif;
    font-size: 44px;
    white-space: nowrap;
    color: var(--muted);
  }
  .volume strong { color: var(--ink); font-weight: 500; }
  .base-band {
    position: absolute; left: 0; right: 0; bottom: 12px; height: 6px;
    background: var(--base-band);
  }
</style>
</head>
<body>
  <div class="seal-strip"><span>Tipplecats Booze</span></div>

  <section class="label">
    <svg class="label-edge top" viewBox="0 0 760 14" preserveAspectRatio="none">
      <path d="M0 14 Q9.5 0 19 14 T38 14 T57 14 T76 14 T95 14 T114 14 T133 14 T152 14 T171 14 T190 14 T209 14 T228 14 T247 14 T266 14 T285 14 T304 14 T323 14 T342 14 T361 14 T380 14 T399 14 T418 14 T437 14 T456 14 T475 14 T494 14 T513 14 T532 14 T551 14 T570 14 T589 14 T608 14 T627 14 T646 14 T665 14 T684 14 T703 14 T722 14 T741 14 T760 14 Z" fill="#f4f2da"/>
    </svg>

    <div class="herb-artwork" role="img" aria-label="Botanical illustration of flowering thyme sprigs"></div>

    <div class="brand">
      <div class="brand-name"><span class="dot"></span>TIPPLECATS</div>
      <div class="brand-tagline">HAND CRAFTED SPIRITS</div>
    </div>

    <h1 class="product-type">LONDON DRY GIN</h1>

    <p class="description">Finely distilled herbal gin<br>balanced mix of botanicals<br>with thyme as ruler.</p>

    <div class="spec-table">
      <div class="flavour">Thymewise</div>
      <div class="spec-row">
        <div class="batch">NO.<br>1</div>
        <div class="category">DISTILLED SPIRIT</div>
        <div class="volume"><strong>500ml</strong> • 38.0% vol. alc.</div>
      </div>
    </div>

    <div class="base-band"></div>

    <svg class="label-edge bottom" viewBox="0 0 760 14" preserveAspectRatio="none">
      <path d="M0 0 Q9.5 14 19 0 T38 0 T57 0 T76 0 T95 0 T114 0 T133 0 T152 0 T171 0 T190 0 T209 0 T228 0 T247 0 T266 0 T285 0 T304 0 T323 0 T342 0 T361 0 T380 0 T399 0 T418 0 T437 0 T456 0 T475 0 T494 0 T513 0 T532 0 T551 0 T570 0 T589 0 T608 0 T627 0 T646 0 T665 0 T684 0 T703 0 T722 0 T741 0 T760 0 Z" fill="#f4f2da"/>
    </svg>
  </section>
</body>
</html>
```